Silver Heron Construction Services

Create a business card for my business consulting company
Danielle Vesk, Founder and CEO
4816 Alder Brook Way, Ste 100
Denver, CO. 80451
303.782.4190 cell
dvesk@silverheronconst.example
www.silverheronconst.example

Target Market(s)

Private Equity and Construction Companies

Industry/Entity Type

Business / Sales Consulting

Contact Information for Business Card

Tag Line that says "Where The Road To Success Is Always Under Construction"

Requirements
Must have
• Logo on both sides of the card.
Nice to have
• Add tagline to the same side of the card as my name and contact info

```html
<!DOCTYPE html>
<html lang="en">
<head>
<meta charset="utf-8">
<title>Silver Heron Construction Services – Business Card</title>
<link rel="stylesheet" href="https://fonts.googleapis.com/css2?family=Jost:wght@400;500;600&display=swap">
<style>
  :root {
    --backdrop: #e9e6e6;
    --card: #bdbdbd;
    --ink: #0d0d0d;
    --band: #c9c9c9;
    --font: "Jost", "Futura", sans-serif;
  }
  * { margin: 0; padding: 0; box-sizing: border-box; }
  html, body {
    width: 695px; height: 1200px; overflow: hidden;
    background: var(--backdrop);
    font-family: var(--font);
    color: var(--ink);
  }
  .sheet {
    position: relative; width: 695px; height: 1200px;
  }
  .card {
    position: absolute; left: 48px; width: 600px; height: 346px;
    background: var(--card);
    overflow: hidden;
  }
  .card--front { top: 150px; }
  .card--back { top: 640px; }
  .card__shapes {
    position: absolute; inset: 0; width: 100%; height: 100%;
  }
  .wordmark {
    position: absolute; text-align: center;
    font-weight: 600; color: var(--ink); text-transform: uppercase;
    line-height: 1;
  }
  .wordmark__rule {
    display: block; height: 2px; background: var(--ink); margin: 6px auto;
  }
  .card--front .wordmark {
    left: 0; right: 0; top: 118px;
  }
  .card--front .wordmark__name { font-size: 34px; letter-spacing: 0.5px; }
  .card--front .wordmark__sub { font-size: 12px; letter-spacing: 2.5px; }
  .card--front .wordmark__rule { width: 290px; }
  .card--back .wordmark {
    right: 22px; top: 52px; width: 150px;
  }
  .card--back .wordmark__name { font-size: 15px; }
  .card--back .wordmark__sub { font-size: 5.5px; letter-spacing: 1.2px; }
  .card--back .wordmark__rule { width: 140px; height: 1px; margin: 3px auto; }
  .person {
    position: absolute; left: 21px; top: 22px;
  }
  .person__name { font-size: 25px; font-weight: 500; line-height: 1.1; }
  .person__title {
    font-size: 14px; font-weight: 400; letter-spacing: 1.6px;
    margin-left: 9px;
  }
  .contact {
    position: absolute; left: 0; right: 0; top: 164px;
    text-align: center; font-size: 14.5px; font-weight: 500;
    letter-spacing: 1.2px; line-height: 1.35;
  }
  .contact__line { display: block; }
  .contact__line--phone { margin-bottom: 10px; }
  .contact__sep {
    display: inline-block; width: 1px; height: 16px; background: var(--ink);
    vertical-align: -3px; margin: 0 5px;
  }
  .contact__pin { width: 9px; height: 11px; vertical-align: -1px; margin-right: 4px; }
  .tagline {
    position: absolute; left: 0; right: 0; top: 293px; height: 21px;
    text-align: center; font-size: 13.5px; font-weight: 500;
    letter-spacing: 3.4px; line-height: 21px;
  }
</style>
</head>
<body>
<main class="sheet">

  <section class="card card--front" aria-label="Card front">
    <svg class="card__shapes" viewBox="0 0 600 346" preserveAspectRatio="none" aria-hidden="true">
      <polygon points="0,201 0,346 220,346" fill="var(--ink)"/>
      <polygon points="600,200 600,346 382,346" fill="var(--ink)"/>
    </svg>
    <div class="wordmark">
      <span class="wordmark__name">Silver Heron</span>
      <span class="wordmark__rule"></span>
      <span class="wordmark__sub">Construction Services</span>
    </div>
  </section>

  <section class="card card--back" aria-label="Card back">
    <svg class="card__shapes" viewBox="0 0 600 346" preserveAspectRatio="none" aria-hidden="true">
      <polygon points="0,201 0,346 214,346" fill="var(--ink)"/>
      <polygon points="600,201 600,346 382,346" fill="var(--ink)"/>
      <rect x="0" y="293" width="600" height="21" fill="var(--band)"/>
      <rect x="0" y="314" width="600" height="2" fill="#7a7a7a"/>
    </svg>

    <div class="person">
      <h1 class="person__name">Danielle Vesk</h1>
      <p class="person__title">Founder and CEO</p>
    </div>

    <div class="wordmark">
      <span class="wordmark__name">Silver Heron</span>
      <span class="wordmark__rule"></span>
      <span class="wordmark__sub">Construction Services</span>
    </div>

    <address class="contact" style="font-style: normal;">
      <span class="contact__line contact__line--phone">303.782.4190<span class="contact__sep"></span>dvesk@silverheronconst.example</span>
      <span class="contact__line"><svg class="contact__pin" viewBox="0 0 9 11" aria-hidden="true"><circle cx="4.5" cy="3.5" r="2.6" fill="none" stroke="var(--ink)" stroke-width="1.4"/><path d="M4.5 6.5 L4.5 9 M1 10.2 H8" stroke="var(--ink)" stroke-width="1.4"/></svg>4816 Alder Brook Way, Ste 100</span>
      <span class="contact__line">Denver, CO. 80451</span>
    </address>

    <p class="tagline">The Road To Success Is Always Under Construction</p>
  </section>

</main>
</body>
</html>
```